依頼詳細
汐凪商店街の中には色んなお店がありますので、
目立つような看板で分かりやすいものが
出来たらと思っていますので、
宜しくお願いします
記載項目
上の看板部分
w1500×h2400
下のテント部分
w1800×h 300
です。
希望イメージ
シンプル 複雑
単色 カラフル
暗い 明るい
日常 高級
遊び心 厳粛
未来的 伝統的
女性的 男性的
希望する色
納品ファイル
補足説明
商品が分かり写真みたいな
看板にしたいと思っていますので
宜しくお願いします
■ 選んだ理由

商店街の中のお店ということもあり、シンプルで分かりやすいのと、色合い等が気にいったので当選することに決めました。

■ 提案者全員のお礼・コメント

この度は皆さんから色んなご提案をいただき
有り難く思い感謝しております。

どれも素敵なデザインだったと思っております。

今後も何かを依頼するときがあると思いますが
宜しくお願いします。

```html
<!DOCTYPE html>
<html lang="ja">
<head>
<meta charset="utf-8">
<title>潮丸 磯の香り揚げ 看板</title>
<link rel="stylesheet" href="https://fonts.googleapis.com/css2?family=Dela+Gothic+One&family=Shippori+Mincho+B1:wght@800&display=swap">
<style>
  :root {
    --sign-brown: #3b1f14;
    --octopus-red: #d8202a;
    --paper-white: #ffffff;
    --ink-black: #1a1210;
    --fry-gold: #d9a25a;
    --fry-light: #f1cf8e;
    --fry-dark: #a66a2e;
    --stick-tan: #e6cfa3;
    --awning-grey: #e9e6e2;
  }
  * { margin: 0; padding: 0; box-sizing: border-box; }
  html, body { width: 754px; height: 1200px; overflow: hidden; background: var(--awning-grey); }
  .canvas { position: relative; width: 754px; height: 1200px; background: var(--awning-grey); }

  .signboard {
    position: absolute; left: 0; top: 0; width: 754px; height: 1085px;
    background: var(--sign-brown); overflow: hidden;
  }
  .octopus-art { position: absolute; inset: 0; width: 100%; height: 100%; }

  .tagline {
    position: absolute; left: 482px; top: 14px;
    writing-mode: vertical-rl;
    font-family: "Shippori Mincho B1", serif; font-weight: 800;
    font-size: 50px; letter-spacing: 4px; line-height: 1; color: var(--paper-white);
  }
  .shop-name {
    position: absolute; left: 40px; top: 110px; width: 420px;
    font-family: "Shippori Mincho B1", serif; font-weight: 800;
    font-size: 190px; line-height: 1; letter-spacing: 6px;
    color: var(--paper-white); text-align: center;
  }

  .photo-skewer {
    position: absolute; left: 232px; top: 380px; width: 118px; height: 630px;
    border-radius: 40px;
    background: linear-gradient(90deg, var(--fry-dark), var(--fry-gold) 35%, var(--fry-light) 60%, var(--fry-gold) 85%, var(--fry-dark));
    transform: rotate(21deg);
  }
  .photo-stick {
    position: absolute; left: 138px; top: 930px; width: 10px; height: 170px;
    background: var(--stick-tan); transform: rotate(21deg);
  }
  .photo-takoten {
    position: absolute; left: 400px; top: 690px; width: 390px; height: 380px;
    border-radius: 50%;
    background: radial-gradient(circle at 45% 40%, var(--fry-light), var(--fry-gold) 60%, var(--fry-dark));
  }

  .menu-tag {
    position: absolute; background: var(--paper-white); color: var(--ink-black);
    font-family: "Dela Gothic One", sans-serif; line-height: 1;
    display: flex; align-items: center; justify-content: center;
  }
  .menu-tag.takobo {
    left: 48px; top: 515px; width: 66px; height: 150px;
    writing-mode: vertical-rl; font-size: 40px;
    border-radius: 6px 18px 10px 20px;
  }
  .menu-tag.takoten {
    left: 478px; top: 648px; width: 140px; height: 64px; font-size: 38px;
    border-radius: 18px 6px 20px 8px;
  }

  .awning {
    position: absolute; left: 0; top: 1125px; width: 754px; height: 64px;
    background: var(--paper-white); overflow: hidden;
  }
  .awning-octopus { position: absolute; right: 0; top: 0; width: 180px; height: 64px; }
  .awning-tag {
    position: absolute; top: 17px; height: 30px; padding: 0 6px;
    border: 2px solid var(--ink-black); background: var(--paper-white);
    font-family: "Dela Gothic One", sans-serif; font-size: 18px; line-height: 26px; color: var(--ink-black);
  }
  .awning-tag.takobo { left: 8px; }
  .awning-tag.takoten { left: 92px; }
  .awning-tagline {
    position: absolute; left: 190px; top: 14px;
    font-family: "Shippori Mincho B1", serif; font-weight: 800; font-size: 28px; line-height: 36px; color: var(--ink-black);
  }
  .awning-name {
    position: absolute; left: 390px; top: 6px;
    font-family: "Shippori Mincho B1", serif; font-weight: 800;
    font-size: 44px; line-height: 52px; color: var(--ink-black);
  }
</style>
</head>
<body>
<main class="canvas">
  <section class="signboard">
    <svg class="octopus-art" viewBox="0 0 754 1085" role="img" aria-label="赤いタコのイラスト">
      <path fill="var(--octopus-red)" d="M40 0 H560 C600 120 560 260 470 330 C600 300 700 380 754 460 V700 C690 560 600 520 520 560 C460 600 380 560 330 470 C260 560 120 600 0 560 V130 C20 80 30 30 40 0 Z"/>
      <path fill="var(--octopus-red)" d="M620 0 H754 V260 C700 200 650 130 620 0 Z"/>
    </svg>
    <div class="tagline">磯の香り揚げ</div>
    <h1 class="shop-name">潮丸</h1>
    <div class="photo-takoten" role="img" aria-label="タコ天の写真"></div>
    <div class="photo-stick" role="img" aria-label="串"></div>
    <div class="photo-skewer" role="img" aria-label="タコ棒の写真"></div>
    <div class="menu-tag takobo">タコ棒</div>
    <div class="menu-tag takoten">タコ天</div>
  </section>

  <section class="awning">
    <span class="awning-tag takobo">タコ棒</span>
    <span class="awning-tag takoten">タコ天</span>
    <span class="awning-tagline">磯の香り揚げ</span>
    <span class="awning-name">潮丸</span>
    <svg class="awning-octopus" viewBox="0 0 180 64" role="img" aria-label="赤いタコのイラスト">
      <path fill="var(--octopus-red)" d="M20 64 C30 30 60 8 100 6 C140 4 170 24 180 40 V64 Z"/>
    </svg>
  </section>
</main>
</body>
</html>
```